Copperleaf Motorized Shade Business Card

Hello, we've had our logo made. Now we are looking for a clean and cool looking business card. One side can just be the logo with any design elements that might look good with it. The other side will be Name, Phone Number and Email. There will not be an address on the card.

```html
<!DOCTYPE html>
<html lang="en">
<head>
<meta charset="utf-8">
<title>Copperleaf Motorized Shade – Business Card</title>
<link rel="stylesheet" href="https://fonts.googleapis.com/css2?family=Bebas+Neue&family=Libre+Franklin:wght@400&display=swap">
<style>
  :root {
    --navy: #003c74;
    --sun: #fcc30e;
    --sky: #00aeef;
    --paper: #ffffff;
    --ink: #1f2328;
    --backdrop: #dde8f0;
  }
  * { margin: 0; padding: 0; box-sizing: border-box; }
  html, body { width: 1200px; height: 1200px; overflow: hidden; }
  body { background: var(--backdrop); position: relative; font-family: "Libre Franklin", sans-serif; }

  .card { position: absolute; left: 283px; width: 634px; height: 362px; overflow: hidden; }
  .card--front { top: 174px; background: var(--paper); }
  .card--back { top: 609px; background: var(--navy); }

  .brand { position: absolute; display: flex; align-items: flex-start; gap: 10px; font-family: "Bebas Neue", sans-serif; font-weight: 400; }
  .brand__mark { background: var(--sun); flex: none; }
  .brand__name { display: flex; flex-direction: column; line-height: 0.9; }
  .brand__main { letter-spacing: 1px; }
  .brand__sub { letter-spacing: 4px; }

  .card--front .brand { left: 35px; top: 58px; color: var(--navy); }
  .card--front .brand__mark { width: 22px; height: 22px; margin-top: 6px; }
  .card--front .brand__main { font-size: 58px; }
  .card--front .brand__sub { font-size: 20px; }

  .holder { position: absolute; right: 28px; top: 174px; text-align: right; }
  .holder__name { font-family: "Bebas Neue", sans-serif; font-size: 33px; line-height: 1; color: var(--navy); }
  .holder__role { font-size: 16px; color: var(--ink); margin-top: 4px; }
  .holder-tab { position: absolute; right: 0; top: 175px; width: 21px; height: 44px; background: var(--navy); }

  .contacts { position: absolute; left: 35px; top: 232px; list-style: none; font-size: 16px; color: var(--ink); }
  .contacts li { display: flex; align-items: center; gap: 8px; height: 21px; }
  .contacts svg { width: 11px; height: 11px; fill: var(--navy); }

  .wave { position: absolute; left: 0; top: 0; width: 634px; height: 362px; }

  .card--back .brand { left: 50%; top: 50%; transform: translate(-50%, -50%); color: var(--paper); }
  .card--back .brand__mark { width: 40px; height: 40px; margin-top: 14px; }
  .card--back .brand__main { font-size: 116px; }
  .card--back .brand__sub { font-size: 34px; letter-spacing: 9px; }
</style>
</head>
<body>
  <section class="card card--front">
    <svg class="wave" viewBox="0 0 634 362" aria-hidden="true">
      <path d="M40,308 C250,293 470,316 597,362" fill="none" stroke="var(--sun)" stroke-width="4"/>
      <path d="M0,314 C210,302 440,318 590,362 L0,362 Z" fill="var(--navy)"/>
    </svg>

    <div class="brand">
      <span class="brand__mark"></span>
      <span class="brand__name">
        <span class="brand__main">Copperleaf</span>
        <span class="brand__sub">Motorized Shade</span>
      </span>
    </div>

    <div class="holder">
      <p class="holder__name">Daniel Reed Carter</p>
      <p class="holder__role">Manager / Owner</p>
    </div>
    <span class="holder-tab"></span>

    <ul class="contacts">
      <li>
        <svg viewBox="0 0 24 24"><path d="M6.6 10.8a15.1 15.1 0 0 0 6.6 6.6l2.2-2.2a1 1 0 0 1 1-.25 11.4 11.4 0 0 0 3.6.57 1 1 0 0 1 1 1V20a1 1 0 0 1-1 1A17 17 0 0 1 3 4a1 1 0 0 1 1-1h3.5a1 1 0 0 1 1 1c0 1.25.2 2.45.57 3.57a1 1 0 0 1-.25 1z"/></svg>
        <span>+1 555 018 2746</span>
      </li>
      <li>
        <svg viewBox="0 0 24 24"><path d="M2 5h20v14H2z M4 7v.5l8 5.5 8-5.5V7z" fill-rule="evenodd"/></svg>
        <span>dcarter@copperleaf.com</span>
      </li>
    </ul>
  </section>

  <section class="card card--back">
    <div class="brand">
      <span class="brand__mark"></span>
      <span class="brand__name">
        <span class="brand__main">Copperleaf</span>
        <span class="brand__sub">Motorized Shade</span>
      </span>
    </div>
  </section>
</body>
</html>
```